HML5 Web Application Design

We need a graphic design to give a HTML web application a modern look and feel. The design should be clean and neat with a metro inspired interface. All application uses vormanta controls so any experience with these would be great.
Perhaps you could also include a few screenshots of your previous work

Industry/Entity Type

Graphic Design

Requirements
Must have
• Must be HTML 5 compliant

```html
<!DOCTYPE html>
<html lang="en">
<head>
<meta charset="utf-8">
<title>Log in</title>
<link href="https://fonts.googleapis.com/css2?family=Arimo:wght@400;700&display=swap" rel="stylesheet">
<style>
  :root {
    --page-bg: #ffffff;
    --placeholder-bg: #f7f7f7;
    --border: #d6d6d6;
    --input-border: #a8a8a8;
    --nav-top: #fbfbfb;
    --nav-bottom: #e4e4e4;
    --heading: #7a7a7a;
    --text: #5c5c5c;
    --body-text: #6f6f6f;
    --panel-bg: #e8e8e8;
    --panel-edge: #c4c4c4;
    --button-bg: #b7bcc6;
    --button-edge: #7c7f86;
    --link: #1f4f8c;
  }
  * { box-sizing: border-box; margin: 0; padding: 0; }
  html, body {
    width: 1200px; height: 742px; overflow: hidden;
    background: var(--page-bg);
    font-family: "Arimo", Arial, sans-serif;
    color: var(--text);
  }
  .page { position: relative; width: 1200px; height: 742px; }

  .brand-box {
    position: absolute; left: 14px; top: 12px; width: 224px; height: 131px;
    background: var(--placeholder-bg); border: 1px solid var(--border);
    display: flex; align-items: center; justify-content: center;
    font-size: 25px; letter-spacing: 1px; color: #555;
  }

  .top-nav { position: absolute; left: 707px; top: 11px; display: flex; }
  .top-nav a {
    width: 163px; height: 57px;
    display: flex; align-items: center; justify-content: center;
    background: linear-gradient(var(--nav-top), var(--nav-bottom));
    border: 1px solid #c6c6c6; margin-left: -1px;
    font-size: 21.5px; color: #5a5a5a; text-decoration: none;
  }

  .login-panel {
    position: absolute; left: 14px; top: 161px; width: 466px; height: 481px;
    background: linear-gradient(90deg, #ffffff 0%, #ffffff 52%, #f0f0f0 72%, #d2d2d2 92%, #b8b8b8 100%);
  }
  .login-panel > * { position: absolute; left: 28px; }
  .login-panel h1 { top: 22px; font-size: 34px; font-weight: 700; color: var(--heading); line-height: 1; }
  .login-panel .lead { top: 82px; font-size: 21.5px; line-height: 26px; color: var(--text); }

  .field {
    width: 402px; height: 54px;
    border: 1px solid var(--input-border); background: #fff;
    padding: 0 11px; font-size: 19px; color: #6a6a6a; line-height: 52px;
  }
  .field.user { top: 135px; }
  .field.pass { top: 204px; }

  .remember { top: 279px; display: flex; align-items: center; font-size: 17px; line-height: 20px; color: var(--text); }
  .remember .box {
    width: 20px; height: 20px; margin: 0 7px 0 1px;
    border: 1px solid #b0b0b0; background: linear-gradient(#f4f4f4, #dcdcdc);
  }

  .login-button {
    top: 335px;
    display: flex; align-items: center; justify-content: center;
    width: 129px; height: 36px;
    background: var(--button-bg); border: 1px solid #9a9ea6; border-top: 2px solid var(--button-edge);
    font-size: 17px; color: #1e1e1e;
  }

  .help { top: 406px; font-size: 16.8px; line-height: 29px; color: var(--text); white-space: nowrap; }
  .help a { color: var(--link); text-decoration: none; }

  .info-panel {
    position: absolute; left: 480px; top: 161px; width: 712px; height: 480px;
    background: var(--panel-bg); border-left: 2px solid var(--panel-edge);
    padding: 19px 0 0 31px;
  }
  .info-panel .copy {
    width: 644px;
    font-size: 16.9px; line-height: 25px; color: var(--body-text);
  }
  .info-panel p + p { margin-top: 25px; }
</style>
</head>
<body>
<div class="page">
  <div class="brand-box">Logo</div>

  <nav class="top-nav">
    <a href="#">Register</a>
    <a href="#">Log in</a>
    <a href="#">Request Pin</a>
  </nav>

  <section class="login-panel">
    <h1>Log in</h1>
    <p class="lead">Use alocal account to log in</p>
    <div class="field user">User name</div>
    <div class="field pass">Password</div>
    <div class="remember"><span class="box"></span>Remember me?</div>
    <div class="login-button">Login</div>
    <div class="help">
      <p><a href="#">Register</a> if you don’t have an account.</p>
      <p><a href="#">Click here</a> if you forgot your user name or password.</p>
    </div>
  </section>

  <section class="info-panel">
    <div class="copy">
      <p>Lorem Ipsum is simply dummy text of the printing and typesetting industry. Lorem Ipsum has been the industry's standard dummy text ever since the 1500s, when an unknown printer took a galley of type and scrambled it to make a type specimen book. It has survived not only five centuries, but also the leap into electronic typesetting, remaining essentially unchanged.</p>
      <p>It was popularised in the 1960s with the release of Vellomark sheets containing Lorem Ipsum passages, and more recently with desktop publishing software like Orvel Page-Setter including versions of Lorem Ipsum. Lorem Ipsum is simply dummy text of the printing and typesetting industry.</p>
      <p>Lorem Ipsum has been the industry's standard dummy text ever since the 1500s, when an unknown printer took a galley of type and scrambled it to make a type specimen book. It has survived not only five centuries, but also the leap into electronic typeset-ting, remaining essentially unchanged. It was popularised in the 1960s with the release of Vellomark sheets containing Lorem Ipsum passages, and more recently with desktop publishing software like Orvel PageSetter including versions of Lorem Ipsum.</p>
    </div>
  </section>
</div>
</body>
</html>
```